Business card design for Automotive workshop

We need a business card for a new automotive repair and tyre shop called Ridgeback Prime Automotive located in New Zealand. We are a clean, modern and fresh workshop and company.

Front needs to feature logo,
my name:
Lachie Westergaard (director)

Address:
48 Marlow Lane
Kereru Bay 3592

Phone: 07 842 1937
Mobile: 027 519 2764
Email: office@ridgebackmotors.co.nz
Website: ridgebackmotors.co.nz

Back needs to feature an area to write down appointment details, date and time.

Also feature a list of jobs and work we do such as,
Vehicle Servicing
All Mechanical Repairs
Warrant of Fitness
Tyres & Wheel Alignments
Automotive Diagnostics
Automotive Parts & Supplies

```html
<!DOCTYPE html>
<html lang="en">
<head>
<meta charset="utf-8">
<title>Ridgeback Prime Automotive – Business Card</title>
<link rel="stylesheet" href="https://fonts.googleapis.com/css2?family=Roboto:wght@400;700&display=swap">
<style>
  :root {
    --backdrop: #2b2522;
    --card: #1c1c1d;
    --red: #e31e24;
    --white: #f4f4f4;
    --muted: #4a4a4c;
    --dots: #bdbdbd;
  }
  * { box-sizing: border-box; margin: 0; padding: 0; }
  html, body { width: 1200px; height: 795px; overflow: hidden; }
  body {
    background: var(--backdrop);
    font-family: "Roboto", Arial, sans-serif;
    color: var(--white);
    display: flex;
    align-items: center;
    justify-content: center;
    gap: 40px;
  }
  .card {
    width: 540px;
    height: 309px;
    background: var(--card);
    border-radius: 8px;
    box-shadow: 0 14px 30px rgba(0,0,0,.5);
    position: relative;
    overflow: hidden;
  }

  /* Back */
  .card-back .brand {
    position: absolute; top: 26px; left: 0; right: 0;
    text-align: center;
    font-size: 25px; font-weight: 700; letter-spacing: 2px;
    color: var(--muted);
    text-transform: uppercase;
  }
  .services {
    position: absolute; top: 88px; left: 40px; right: 30px;
    display: grid; grid-template-columns: 1fr 1fr; column-gap: 20px;
  }
  .services ul { list-style: none; }
  .services li {
    font-size: 13px; line-height: 20px; padding-left: 14px; position: relative;
    white-space: nowrap;
  }
  .services li::before {
    content: ""; position: absolute; left: 0; top: 6px;
    width: 7px; height: 7px; border-radius: 50%; background: var(--red);
  }
  .services .col-right { padding-top: 34px; }
  .appointment {
    position: absolute; left: 40px; right: 40px; top: 200px;
  }
  .appointment .line {
    border-bottom: 1px dashed var(--dots); height: 24px;
  }
  .appointment .label {
    color: var(--red); font-size: 13px; margin-top: 10px; text-align: center;
  }

  /* Front */
  .card-front .brand {
    position: absolute; top: 44px; right: 32px;
    display: flex; align-items: center; gap: 10px;
    font-size: 26px; font-weight: 700; letter-spacing: 2px;
    color: var(--red); text-transform: uppercase;
    white-space: nowrap;
  }
  .card-front .brand .mark {
    width: 14px; height: 14px; background: var(--red);
  }
  .card-front .tagline-rule {
    position: absolute; top: 88px; right: 32px; width: 360px; height: 2px;
    background: var(--white); opacity: .85;
  }
  .details {
    position: absolute; top: 140px; left: 30px; right: 24px;
    display: grid; grid-template-columns: 220px 2px 1fr; column-gap: 16px;
  }
  .person { text-align: right; }
  .person .name { color: var(--red); font-weight: 700; font-size: 19px; margin-bottom: 6px; white-space: nowrap; }
  .person p { font-size: 14px; line-height: 20px; }
  .divider { background: var(--red); width: 2px; height: 118px; }
  .contacts { list-style: none; }
  .contacts li {
    display: flex; align-items: center; gap: 10px;
    font-size: 14px; line-height: 24px; white-space: nowrap;
  }
  .contacts svg { width: 14px; height: 14px; flex: none; }
</style>
</head>
<body>

  <section class="card card-back" aria-label="Card back">
    <div class="brand">Ridgeback Prime Automotive</div>
    <div class="services">
      <ul class="col-left">
        <li>Vehicle Servicing</li>
        <li>All Mechanical Repairs</li>
        <li>Warrant of Fitness</li>
      </ul>
      <ul class="col-right">
        <li>Tyres &amp; Wheel Alignments</li>
        <li>Automotive Diagnostics</li>
        <li>Automotive Parts &amp; Supplies</li>
      </ul>
    </div>
    <div class="appointment">
      <div class="line"></div>
      <div class="line"></div>
      <div class="line"></div>
      <p class="label">Appointment Details:</p>
    </div>
  </section>

  <section class="card card-front" aria-label="Card front">
    <div class="brand"><span class="mark"></span>Ridgeback Prime Automotive</div>
    <div class="tagline-rule"></div>
    <div class="details">
      <div class="person">
        <p class="name">Lachie Westergaard</p>
        <p>Director</p>
        <p>48 Marlow Lane</p>
        <p>Kereru Bay 3592</p>
      </div>
      <div class="divider"></div>
      <ul class="contacts">
        <li>
          <svg viewBox="0 0 14 14"><rect x="3.5" y="1" width="7" height="12" rx="1.2" fill="none" stroke="#e31e24" stroke-width="1.4"/><circle cx="7" cy="11" r=".8" fill="#e31e24"/></svg>
          027 519 2764
        </li>
        <li>
          <svg viewBox="0 0 14 14"><path d="M3 1.5l2 .3 1 3-1.5 1.2a7 7 0 0 0 3.5 3.5L9.2 8l3 1 .3 2-1.5 1.5C6 12.5 1.5 8 1.5 3z" fill="#e31e24"/></svg>
          07 842 1937
        </li>
        <li>
          <svg viewBox="0 0 14 14"><rect x="1" y="3" width="12" height="8.5" fill="#e31e24"/><path d="M1 3l6 5 6-5" fill="none" stroke="#1c1c1d" stroke-width="1.2"/></svg>
          office@ridgebackmotors.co.nz
        </li>
        <li>
          <svg viewBox="0 0 14 14"><circle cx="7" cy="7" r="5.8" fill="none" stroke="#e31e24" stroke-width="1.4"/><ellipse cx="7" cy="7" rx="2.4" ry="5.8" fill="none" stroke="#e31e24" stroke-width="1.1"/><path d="M1.3 7h11.4" stroke="#e31e24" stroke-width="1.1"/></svg>
          www.ridgebackmotors.co.nz
        </li>
      </ul>
    </div>
  </section>

</body>
</html>
```